Business Card Design

I want a simple and modern design, but also something very catching to the eye.

Also is there anyway that the text can be adjusted or changed so that I may make cards for other employees? If so, please make it so that I may edit the texts at a future date.

Reason: I need all designers to update the business card with my update information.

Industry/Entity Type

Business

Contact Information for Business Card

Owner: Marcus Halvorsen
Company Name: Play Brixo
Phone # :555-203-7841
Website: playbrixoshop.example
Email: marc@playbrixoshop.example

```html
<!DOCTYPE html>
<html lang="en">
<head>
<meta charset="utf-8">
<title>Play Brixo — Business Card</title>
<link rel="stylesheet" href="https://fonts.googleapis.com/css2?family=Open+Sans:wght@400;600;700&display=swap">
<style>
  :root {
    --backdrop: #e9e6e1;
    --card-white: #ffffff;
    --teal: #1fa3b3;
    --red: #e0393a;
    --name-teal: #5bbfc9;
    --ink: #333333;
    --ink-soft: #666666;
    --brand: #1fa3b3;
  }
  * { box-sizing: border-box; margin: 0; padding: 0; }
  html, body {
    width: 1200px;
    height: 1023px;
    overflow: hidden;
    background: var(--backdrop);
    font-family: "Open Sans", Arial, sans-serif;
  }
  .stage {
    width: 1200px;
    height: 1023px;
    display: flex;
    align-items: center;
    justify-content: center;
  }
  .card {
    position: relative;
    width: 910px;
    height: 520px;
    background: var(--card-white);
    border-radius: 6px;
    overflow: hidden;
    box-shadow: 0 14px 40px rgba(0,0,0,0.18);
  }
  .card-bands {
    position: absolute;
    inset: 0;
    width: 100%;
    height: 100%;
  }
  .card-content {
    position: absolute;
    left: 90px;
    top: 118px;
    right: 70px;
  }
  .brand {
    display: flex;
    align-items: center;
    gap: 18px;
  }
  .brand-mark {
    width: 58px;
    height: 58px;
    background: var(--red);
    border-radius: 6px;
    flex: none;
  }
  .brand-name {
    font-size: 64px;
    font-weight: 700;
    color: var(--brand);
    line-height: 1;
  }
  .details {
    margin-top: 28px;
    margin-left: 150px;
  }
  .person-name {
    font-size: 34px;
    font-weight: 600;
    color: var(--name-teal);
    line-height: 1.15;
  }
  .person-role {
    margin-top: 2px;
    font-size: 20px;
    font-weight: 400;
    color: var(--ink-soft);
  }
  .contact-list {
    list-style: none;
    margin-top: 22px;
  }
  .contact-item {
    font-size: 21px;
    font-weight: 600;
    color: var(--ink);
    line-height: 1.5;
    white-space: nowrap;
  }
</style>
</head>
<body>
  <main class="stage">
    <article class="card">
      <svg class="card-bands" viewBox="0 0 910 520" preserveAspectRatio="none" aria-hidden="true">
        <path d="M0 0 H910 V60 Q455 10 0 40 Z" fill="var(--teal)"/>
        <path d="M0 40 Q455 10 910 60 V68 Q455 20 0 50 Z" fill="var(--red)"/>
        <path d="M0 520 H910 V440 Q455 500 0 470 Z" fill="var(--teal)"/>
        <path d="M0 470 Q455 500 910 440 V430 Q455 490 0 460 Z" fill="var(--red)"/>
      </svg>
      <div class="card-content">
        <div class="brand">
          <span class="brand-mark"></span>
          <span class="brand-name">Play Brixo</span>
        </div>
        <div class="details">
          <p class="person-name">Marcus Halvorsen</p>
          <p class="person-role">Owner</p>
          <ul class="contact-list">
            <li class="contact-item">Phone: 555-203-7841</li>
            <li class="contact-item">Email: marc@playbrixoshop.example</li>
            <li class="contact-item">Web: playbrixoshop.example</li>
          </ul>
        </div>
      </div>
    </article>
  </main>
</body>
</html>
```